Car wellness, we make cars new and shiny

We need an design for a "small" ad that is published inside a magazine on a holiday tour bus. The audience is mostly 60+ years old.
We are a tinsmith's workshop and painter's shop company with a passion for shiny cars. We love to fix all the little scratches and dents a car gets over time and make it look new again.
The motto is car wellness (Wellness für Ihr Auto).
The ad has to be in German. If you are not fluent in German you may use the text in the example but feel free to use an appropriate font.
The COUPON is our call to action: We want the customer to call us. And it includes an offering of free get and return service of the customers car. It also inclueds some restrictions to the free service (proximity and valid until date).
Things that can't be changed are:
- the logo itself (the position, size and orientation are free)
- the color of the dot in the logo
- the size of the ad: 82mm x 118mm
- the magazines size: approx. A4
We expect a print ready result and would like to receive the files in original file format (eps, svg ...).
We hope for an eye-catching ad that drives the attention of the reader.
Car owners, with 60+ years of age.

```html
<!DOCTYPE html>
<html lang="de">
<head>
<meta charset="utf-8">
<title>Karosserie Lindenau – Wellness für Ihr Auto</title>
<link href="https://fonts.googleapis.com/css2?family=Hind:wght@600&family=Krona+One&family=Michroma&display=swap" rel="stylesheet">
<style>
  :root {
    --page: #c8c8c8;
    --orange: #f28a10;
    --orange-deep: #ee7a06;
    --orange-light: #f9b21c;
    --cream: #fff4d6;
    --ink: #222222;
    --white: #ffffff;
    --blue: #1b9be2;
    --yellow: #f7ea00;
    --phone: #f07d0a;
  }
  html, body {
    margin: 0;
    width: 1200px;
    height: 2183px;
    overflow: hidden;
    background: var(--page);
  }
  .ad {
    position: absolute;
    left: 60px;
    top: 314px;
    width: 1080px;
    height: 1554px;
    box-shadow: 0 14px 22px rgba(0,0,0,0.25);
  }
  .logo { font-family: "Hind", sans-serif; font-weight: 600; fill: var(--ink); }
  .headline { font-family: "Michroma", sans-serif; fill: var(--white); font-variant: small-caps; letter-spacing: 1px; }
  .body-copy { font-family: "Michroma", sans-serif; fill: var(--cream); font-variant: small-caps; font-weight: 700; }
  .coupon-title { font-family: "Krona One", sans-serif; fill: var(--ink); }
  .coupon-phone { font-family: "Krona One", sans-serif; fill: var(--phone); }
  .coupon-note { font-family: "Krona One", sans-serif; fill: var(--ink); }
  .coupon-tab { font-family: "Krona One", sans-serif; }
</style>
</head>
<body>
<svg class="ad" viewBox="0 0 816 1174" xmlns="http://www.w3.org/2000/svg">
  <defs>
    <radialGradient id="sunburst" cx="418" cy="420" r="620" gradientUnits="userSpaceOnUse">
      <stop offset="0" stop-color="#fbc22a"/>
      <stop offset="0.55" stop-color="#f7a01a"/>
      <stop offset="1" stop-color="#f28a10"/>
    </radialGradient>
    <linearGradient id="lower" x1="0" y1="0" x2="0" y2="1">
      <stop offset="0" stop-color="#f8a817"/>
      <stop offset="1" stop-color="#f28a10"/>
    </linearGradient>
    <linearGradient id="photoMain" x1="0" y1="0" x2="0" y2="1">
      <stop offset="0" stop-color="#e9e6df"/>
      <stop offset="0.55" stop-color="#a9cfc9"/>
      <stop offset="1" stop-color="#7d7f80"/>
    </linearGradient>
    <linearGradient id="photoSmall" x1="0" y1="0" x2="1" y2="1">
      <stop offset="0" stop-color="#d9d5d0"/>
      <stop offset="1" stop-color="#56504b"/>
    </linearGradient>
    <path id="headlineArc" d="M 128 590 Q 418 820 708 590"/>
  </defs>

  <!-- background -->
  <rect class="backdrop" width="816" height="1174" fill="url(#sunburst)"/>
  <rect class="lower-field" y="553" width="816" height="621" fill="url(#lower)"/>

  <!-- deep orange crescent band with white stripes -->
  <path class="band" d="M 0 553 H 816 V 600 Q 418 900 0 600 Z" fill="var(--orange-deep)"/>
  <path class="stripe" d="M 0 600 Q 418 900 816 600" fill="none" stroke="var(--white)" stroke-width="7"/>
  <path class="stripe-thin" d="M 0 622 Q 418 935 816 622" fill="none" stroke="var(--white)" stroke-width="3"/>

  <!-- logo wordmark -->
  <text class="logo" x="408" y="84" text-anchor="middle" font-size="46">karosserie-lindenau.ch</text>

  <!-- hero photo -->
  <circle cx="418" cy="418" r="257" fill="var(--white)"/>
  <circle cx="418" cy="418" r="249" fill="url(#photoMain)" role="img" aria-label="Photo: mint-green classic car parked in front of a white house"/>

  <!-- headline on arc -->
  <text class="headline" font-size="38">
    <textPath href="#headlineArc" startOffset="50%" text-anchor="middle">Wellness für Ihr Auto</textPath>
  </text>

  <!-- service photos -->
  <circle cx="222" cy="777" r="71" fill="var(--white)"/>
  <circle cx="222" cy="777" r="66" fill="url(#photoSmall)" role="img" aria-label="Photo: damage on a car bumper being inspected"/>
  <circle cx="420" cy="808" r="67" fill="var(--white)"/>
  <circle cx="420" cy="808" r="62" fill="url(#photoSmall)" role="img" aria-label="Photo: damage report filled in next to a car wheel"/>
  <circle cx="612" cy="772" r="68" fill="var(--white)"/>
  <circle cx="612" cy="772" r="63" fill="url(#photoSmall)" role="img" aria-label="Photo: mechanic polishing a car in the workshop"/>

  <!-- body copy -->
  <g class="body-copy" text-anchor="middle" font-size="17">
    <text x="418" y="907">Ob kleinere Kratzer und Beulen</text>
    <text x="418" y="932">oder ein grosseres Malheur, wir verhelfen</text>
    <text x="418" y="957">Ihrem Auto zu neuem Glanz!</text>
  </g>

  <!-- coupon -->
  <g class="coupon">
    <rect x="65" y="990" width="708" height="165" fill="none" stroke="var(--white)" stroke-width="3" stroke-dasharray="2 4"/>
    <g class="scissors" stroke="var(--white)" stroke-width="2.5" fill="none">
      <circle cx="148" cy="982" r="4.5"/>
      <circle cx="148" cy="996" r="4.5"/>
      <path d="M152 984 L188 993 M152 994 L188 985"/>
    </g>
    <rect x="85" y="1008" width="667" height="132" rx="4" fill="var(--white)"/>
    <rect x="85" y="1008" width="67" height="132" fill="var(--blue)"/>
    <rect x="668" y="1008" width="84" height="132" fill="var(--yellow)"/>
    <text class="coupon-tab" transform="translate(128 1074) rotate(-90)" text-anchor="middle" font-size="17" fill="var(--white)">COUPON</text>
    <text class="coupon-tab" transform="translate(703 1074) rotate(-90)" text-anchor="middle" font-size="14" fill="var(--ink)">CODE:</text>
    <text class="coupon-tab" transform="translate(722 1074) rotate(-90)" text-anchor="middle" font-size="11" fill="var(--ink)">Reiseglanz</text>

    <text class="coupon-title" x="410" y="1043" text-anchor="middle" font-size="20">Gratis Hol-&amp; Bring-Service</text>
    <text class="coupon-title" x="410" y="1068" text-anchor="middle" font-size="20">Rufen Sie uns an:</text>

    <g class="phone-icon" stroke="var(--phone)" stroke-width="2" fill="none">
      <path d="M181 1090 q-3 8 6 14 l3 -3 -4 -4 -2 1 q-3 -2 -3 -5 l2 -1 -2 -5 z"/>
    </g>
    <text class="coupon-phone" x="202" y="1105" font-size="19">+41 56 000 1234</text>
    <line x1="459" y1="1088" x2="459" y2="1106" stroke="var(--phone)" stroke-width="2"/>
    <g class="calendar-icon" stroke="var(--phone)" stroke-width="2" fill="none">
      <rect x="480" y="1090" width="15" height="14" rx="1"/>
      <line x1="480" y1="1095" x2="495" y2="1095"/>
    </g>
    <text class="coupon-phone" x="503" y="1105" font-size="16">31.Dez.2021</text>

    <text class="coupon-note" x="410" y="1130" text-anchor="middle" font-size="10.5">Gultig im Umkreis von 50Km um Lindenau bis am</text>
  </g>
</svg>
</body>
</html>
```